Design an Outstanding flyer for my company.

I need a flyer designed for our window tinting company based in Brisbane Queensland Australia. The flyer will be targeting Home tinting. We also do mobile car tinting. Something in regards to this could be incorporated into the flyer as well.
I want it to be 2 sided DL size. Black background.
It really needs to Pop, and be a real attention getter.
It needs to be easy to read.
I have provided a mock up with the info on it from our marketing company. It will need a spellcheck etc to make sure everything is correct.
Everything about it can be changed however you like.
I have also included the company logo.

Lets see what you've got!

Target Market(s)

Home Owners

Industry/Entity Type

Home Improvement

Font styles to use
Other font styles liked:
• Duan Penh

Requirements
Must have
• All the information on the mock up. Clear and easy to read.
• Must Stand Out!

```html
<!DOCTYPE html>
<html lang="en">
<head>
<meta charset="utf-8">
<title>Brightline Window Tinting – DL Flyer</title>
<link rel="stylesheet" href="https://fonts.googleapis.com/css2?family=Cinzel:wght@400;700&family=Libre+Baskerville:wght@700&family=Oswald:wght@600&family=Open+Sans:wght@400&display=swap">
<style>
  :root {
    --page: #ffffff;
    --panel-dark: #231f20;
    --panel-black: #0b0b0b;
    --ink-white: #ffffff;
    --accent-yellow: #fcd51c;
    --chip-ink: #111111;
    --brand-gold: #e3bd1e;
    --strip-light: #c9c9c9;
    --strip-mid: #4a4a4a;
    --strip-dark: #2e2e2e;
  }
  html, body {
    margin: 0;
    padding: 0;
    width: 1200px;
    height: 1200px;
    overflow: hidden;
    background: var(--page);
  }
  .flyer-sheet { display: block; width: 1200px; height: 1200px; }
  .serif-caps { font-family: "Cinzel", "Times New Roman", serif; font-weight: 400; fill: var(--ink-white); }
  .headline-big { font-family: "Libre Baskerville", "Times New Roman", serif; font-weight: 700; fill: var(--accent-yellow); }
  .phone-number { font-family: "Cinzel", "Times New Roman", serif; font-weight: 400; fill: var(--ink-white); }
  .reason-chip rect { fill: var(--accent-yellow); }
  .reason-chip text { font-family: "Oswald", "Arial Narrow", sans-serif; font-weight: 600; font-size: 34px; fill: var(--chip-ink); }
  .brand-name, .brand-tagline { font-family: "Cinzel", "Times New Roman", serif; font-weight: 400; fill: var(--brand-gold); }
  .brand-mark { fill: var(--brand-gold); }
  .web-address { font-family: "Open Sans", Arial, sans-serif; font-weight: 400; font-size: 25px; fill: var(--ink-white); }
  .icon-line { fill: none; stroke: var(--ink-white); stroke-width: 4; }
  .icon-fill { fill: var(--ink-white); }
  .sms-bubble { fill: var(--accent-yellow); }
  .sms-text { font-family: "Oswald", "Arial Narrow", sans-serif; font-weight: 600; font-size: 11px; fill: var(--chip-ink); }
</style>
</head>
<body>
<svg class="flyer-sheet" viewBox="0 0 1500 1500" xmlns="http://www.w3.org/2000/svg">
  <defs>
    <radialGradient id="windowLight" cx="0.72" cy="0.55" r="0.6">
      <stop offset="0" stop-color="#8a8a8a"/>
      <stop offset="0.45" stop-color="#3a3a3a"/>
      <stop offset="1" stop-color="#080808"/>
    </radialGradient>
    <linearGradient id="carPhoto" x1="0" y1="0" x2="0.4" y2="1">
      <stop offset="0" stop-color="#2b2b2b"/>
      <stop offset="0.3" stop-color="#6a6a6a"/>
      <stop offset="0.55" stop-color="#3c3c3c"/>
      <stop offset="0.8" stop-color="#111111"/>
      <stop offset="1" stop-color="#050505"/>
    </linearGradient>
  </defs>

  <!-- Front side -->
  <g class="flyer-front">
    <rect x="36" y="25" width="682" height="1448" fill="var(--panel-dark)"/>
    <rect class="hero-photo" x="36" y="178" width="682" height="757" fill="url(#windowLight)" role="img" aria-label="Sunlight streaming through a tall window onto a bare floor, black and white"/>
    <g class="edge-strip">
      <rect x="684" y="25" width="34" height="153" fill="var(--strip-light)"/>
      <rect x="684" y="178" width="34" height="137" fill="var(--strip-dark)"/>
      <rect x="684" y="605" width="34" height="330" fill="var(--strip-mid)"/>
      <rect x="684" y="935" width="34" height="250" fill="var(--strip-mid)"/>
      <rect x="684" y="1185" width="34" height="288" fill="var(--strip-dark)"/>
    </g>

    <text class="serif-caps" x="72" y="160" font-size="64" textLength="533" lengthAdjust="spacingAndGlyphs">KEEP HEAT OUT</text>
    <text class="serif-caps" x="72" y="214" font-size="40" textLength="472" lengthAdjust="spacingAndGlyphs">BLOCK 99.9% UV RAYS</text>
    <text class="headline-big" x="75" y="385" font-size="118" textLength="330" lengthAdjust="spacingAndGlyphs">SAVE</text>
    <text class="headline-big" x="75" y="522" font-size="118" textLength="533" lengthAdjust="spacingAndGlyphs">MONEY</text>
    <text class="serif-caps" x="72" y="602" font-size="42" textLength="410" lengthAdjust="spacingAndGlyphs">INCREASE PRIVACY</text>

    <text class="serif-caps" x="72" y="960" font-size="36" textLength="507" lengthAdjust="spacingAndGlyphs">CALL BRISBANE’S LEADER IN</text>
    <text class="serif-caps" x="72" y="1006" font-size="36" textLength="576" lengthAdjust="spacingAndGlyphs">HOME WINDOW TINTING NOW:</text>

    <g class="contact-phone">
      <rect class="icon-line" x="164" y="1048" width="34" height="64" rx="6"/>
      <line class="icon-line" x1="166" y1="1058" x2="196" y2="1058"/>
      <line class="icon-line" x1="166" y1="1100" x2="196" y2="1100"/>
      <text class="phone-number" x="226" y="1100" font-size="56" textLength="330" lengthAdjust="spacingAndGlyphs">07 3190 5568</text>
    </g>
    <g class="contact-sms">
      <rect class="icon-line" x="164" y="1139" width="34" height="64" rx="6"/>
      <line class="icon-line" x1="166" y1="1191" x2="196" y2="1191"/>
      <rect class="sms-bubble" x="176" y="1156" width="32" height="20" rx="3"/>
      <text class="sms-text" x="179" y="1171">SMS</text>
      <text class="phone-number" x="226" y="1186" font-size="56" textLength="330" lengthAdjust="spacingAndGlyphs">04 2287 6093</text>
    </g>

    <g class="brand-block">
      <circle class="brand-mark" cx="145" cy="1300" r="46"/>
      <text class="brand-name" x="220" y="1332" font-size="64" textLength="428" lengthAdjust="spacingAndGlyphs">BRIGHTLINE</text>
      <text class="brand-tagline" x="255" y="1360" font-size="16" textLength="392" lengthAdjust="spacing">WINDOW TINTING</text>
    </g>
    <text class="web-address" x="193" y="1423" textLength="327" lengthAdjust="spacingAndGlyphs">www.brightlinetinting.com.au</text>
  </g>

  <!-- Back side -->
  <g class="flyer-back">
    <rect x="765" y="25" width="683" height="1448" fill="var(--panel-black)"/>
    <rect class="hero-photo" x="765" y="25" width="683" height="1448" fill="url(#carPhoto)" role="img" aria-label="Close-up of a glossy car front and headlight, black and white"/>
    <g class="edge-strip">
      <rect x="1414" y="25" width="34" height="290" fill="var(--strip-light)"/>
      <rect x="1414" y="315" width="34" height="290" fill="#6e6e6e"/>
      <rect x="1414" y="605" width="34" height="290" fill="var(--strip-mid)"/>
      <rect x="1414" y="895" width="34" height="290" fill="#3a3a3a"/>
      <rect x="1414" y="1185" width="34" height="288" fill="var(--strip-dark)"/>
    </g>

    <text class="serif-caps" x="803" y="155" font-size="56" textLength="475" lengthAdjust="spacingAndGlyphs">20 REASONS WHY</text>
    <text class="serif-caps" x="803" y="207" font-size="56" textLength="577" lengthAdjust="spacingAndGlyphs">WINDOW TINTING IS</text>
    <text class="serif-caps" x="803" y="258" font-size="56" textLength="515" lengthAdjust="spacingAndGlyphs">PERFECT FOR YOU.</text>

    <g class="reasons-list">
      <g class="reason-chip"><rect x="795" y="335" width="182" height="44"/><text x="802" y="369" textLength="168" lengthAdjust="spacingAndGlyphs">KEEP HEAT OUT</text></g>
      <g class="reason-chip"><rect x="988" y="335" width="264" height="44"/><text x="995" y="369" textLength="250" lengthAdjust="spacingAndGlyphs">BLOCK 99.9% UV RAYS</text></g>
      <g class="reason-chip"><rect x="795" y="389" width="160" height="44"/><text x="802" y="423" textLength="146" lengthAdjust="spacingAndGlyphs">SAVE MONEY</text></g>
      <g class="reason-chip"><rect x="966" y="389" width="234" height="44"/><text x="973" y="423" textLength="220" lengthAdjust="spacingAndGlyphs">INCREASE PRIVACY</text></g>
      <g class="reason-chip"><rect x="795" y="443" width="182" height="45"/><text x="802" y="477" textLength="168" lengthAdjust="spacingAndGlyphs">REDUCE GLARE</text></g>
      <g class="reason-chip"><rect x="993" y="443" width="280" height="45"/><text x="1000" y="477" textLength="266" lengthAdjust="spacingAndGlyphs">REDUCE ENERGY COSTS</text></g>
      <g class="reason-chip"><rect x="795" y="497" width="498" height="45"/><text x="802" y="531" textLength="484" lengthAdjust="spacingAndGlyphs">CONTROL THE AMOUNT OF LIGHT ENTERING</text></g>
      <g class="reason-chip"><rect x="795" y="541" width="153" height="45"/><text x="802" y="576" textLength="139" lengthAdjust="spacingAndGlyphs">YOUR HOME.</text></g>
      <g class="reason-chip"><rect x="795" y="597" width="338" height="44"/><text x="802" y="631" textLength="324" lengthAdjust="spacingAndGlyphs">REDUCE CARBON FOOTPRINT</text></g>
      <g class="reason-chip"><rect x="795" y="651" width="354" height="44"/><text x="802" y="685" textLength="340" lengthAdjust="spacingAndGlyphs">MAKE HOME MORE BEAUTIFUL</text></g>
      <g class="reason-chip"><rect x="795" y="705" width="334" height="45"/><text x="802" y="739" textLength="320" lengthAdjust="spacingAndGlyphs">ELIMINATE HOME HOT SPOTS</text></g>
      <g class="reason-chip"><rect x="795" y="760" width="402" height="44"/><text x="802" y="794" textLength="388" lengthAdjust="spacingAndGlyphs">PROTECT AGAINST BROKEN GLASS</text></g>
      <g class="reason-chip"><rect x="795" y="814" width="225" height="44"/><text x="802" y="848" textLength="211" lengthAdjust="spacingAndGlyphs">REGULATE ENERGY</text></g>
      <g class="reason-chip"><rect x="1031" y="814" width="291" height="44"/><text x="1038" y="848" textLength="277" lengthAdjust="spacingAndGlyphs">PROTECTS UPHOLSTERY</text></g>
      <g class="reason-chip"><rect x="795" y="868" width="556" height="45"/><text x="802" y="902" textLength="542" lengthAdjust="spacingAndGlyphs">IMPROVE EFFECTIVENESS OF ROOF INSULATION.</text></g>
      <g class="reason-chip"><rect x="795" y="922" width="217" height="45"/><text x="802" y="956" textLength="203" lengthAdjust="spacingAndGlyphs">IMPROVE HEALTH.</text></g>
      <g class="reason-chip"><rect x="795" y="977" width="402" height="44"/><text x="802" y="1011" textLength="388" lengthAdjust="spacingAndGlyphs">REDUCES INTERIOR FLOOR FADING.</text></g>
      <g class="reason-chip"><rect x="795" y="1031" width="342" height="45"/><text x="802" y="1065" textLength="328" lengthAdjust="spacingAndGlyphs">ELIMINATE NEED FOR BLINDS.</text></g>
      <g class="reason-chip"><rect x="795" y="1086" width="360" height="44"/><text x="802" y="1120" textLength="346" lengthAdjust="spacingAndGlyphs">STRENGTHEN YOUR WINDOWS.</text></g>
      <g class="reason-chip"><rect x="795" y="1140" width="253" height="45"/><text x="802" y="1174" textLength="239" lengthAdjust="spacingAndGlyphs">INSULATE IN WINTER.</text></g>
      <g class="reason-chip"><rect x="1059" y="1140" width="191" height="45"/><text x="1066" y="1174" textLength="177" lengthAdjust="spacingAndGlyphs">AFFORDABLE.</text></g>
    </g>

    <g class="brand-block">
      <circle class="brand-mark" cx="875" cy="1300" r="46"/>
      <text class="brand-name" x="950" y="1332" font-size="64" textLength="428" lengthAdjust="spacingAndGlyphs">BRIGHTLINE</text>
      <text class="brand-tagline" x="985" y="1360" font-size="16" textLength="392" lengthAdjust="spacing">WINDOW TINTING</text>
    </g>
    <text class="web-address" x="923" y="1423" textLength="327" lengthAdjust="spacingAndGlyphs">www.brightlinetinting.com.au</text>
  </g>
</svg>
</body>
</html>
```